Quellor Health — Premium Telehealth Marketing Website

Quellor Health is a modern, cash-pay telehealth brand offering prescription weight-loss (GLP-1) and sexual-health treatment online, with licensed US providers — no insurance required. We're building a premium, trustworthy direct-to-consumer healthcare brand in the same tier as Tavrin, Ux, and Plimso.

We need a clean, modern, premium marketing website design — warm and trustworthy, not cold or clinical. Think high-end wellness brand: generous whitespace, elegant typography, calm and confident. It should feel medically credible but human and approachable.

WHAT WE NEED DESIGNED (3 core templates that define the whole site):

1. Homepage — the brand showcase that establishes the full visual language (hero, sections, product highlights, how-it-works, trust elements, footer).

2. Product / Treatment page template — a reusable layout for any medication (transparent pricing, how it works, what's included, clinical info, safety, clear call-to-action). We'll reuse this pattern for all treatments.

3. Interior / Content page template — a flexible layout for sub-pages like How It Works, About, Contact, FAQ, and legal pages.

We'll implement the final site ourselves in React/Next.js + Tailwind CSS, so clean, well-structured design (and HTML/CSS if you provide it) is a strong plus.

BRAND DIRECTION (already established — please design within this):

- Logo: lowercase wordmark "quellor." with the period in gold (see attached). Please build the design around this existing logo.
- Colors: deep navy (#0B1B33 and #14315C) with a warm gold accent (#E0A458); soft light backgrounds (#EEF3F9, #FBFCFE).
- Typography: a refined serif for headlines (e.g., Fraunces) paired with a clean sans-serif for body (e.g., Inter).
- Tone: premium, warm, trustworthy, human.

INSPIRATION / QUALITY BAR: Tavrin (tavrin.example), Ux (ux.example), Plimso — the polished DTC healthcare aesthetic. We want that tier of quality, with our own warmer navy-and-gold identity.

Industry/Entity Type

Telemedicine

Coding

Coded - Design and coding required

Number of Pages Required

3 page

Requirements
Nice to have
• Side Scrolling Medictions bar like on Ux.example

```html
<!DOCTYPE html>
<html lang="en">
<head>
<meta charset="utf-8">
<title>Quellor Health — Personalized Treatments</title>
<link rel="stylesheet" href="https://fonts.googleapis.com/css2?family=Gilda+Display&family=Poppins:wght@400;500;600&display=swap">
<style>
:root{
  --navy:#0B1B33;
  --navy-2:#14315C;
  --gold:#E0A458;
  --gold-deep:#C98E45;
  --sky:#EEF3F9;
  --paper:#FBFCFE;
  --warm:#F7F3EF;
  --sand:#F3EADF;
  --ink:#1B2333;
  --muted:#5E6573;
  --line:#E4E7EE;
  --serif:'Gilda Display', Georgia, serif;
  --sans:'Poppins', Arial, sans-serif;
}
*{box-sizing:border-box;margin:0;padding:0}
html,body{width:1200px;height:3816px;overflow:hidden}
body{font-family:var(--sans);color:var(--ink);background:var(--paper);position:relative}
a{color:inherit;text-decoration:none}
.abs{position:absolute}
section,header,footer{position:absolute;left:0;width:1200px}
.serif{font-family:var(--serif);font-weight:400}
.gold{color:var(--gold-deep)}
.btn{display:inline-flex;align-items:center;justify-content:center;gap:10px;border-radius:40px;font-size:13px;font-weight:500}
.btn-navy{background:var(--navy);color:#fff}
.btn-outline{border:1.5px solid var(--navy);color:var(--navy);background:#fff}
.link-arrow{display:inline-flex;align-items:center;gap:10px;font-size:13px;font-weight:500;border-bottom:1px solid #C9CDD6;padding-bottom:6px}
.logo{font-family:var(--serif);color:var(--navy);letter-spacing:-.5px}
.logo span{color:var(--gold)}
.ph{border-radius:inherit}

/* Nav */
.site-nav{top:0;height:74px;background:#F4F5FA}
.site-nav .logo{left:30px;top:10px;font-size:40px}
.nav-links{left:376px;top:28px;display:flex;gap:0;font-size:13.5px;color:var(--ink)}
.nav-links a{position:absolute;white-space:nowrap}
.nav-cta{left:925px;top:16px;width:126px;height:42px;background:var(--gold);color:var(--navy);font-size:13px}
.nav-login{left:1058px;top:16px;width:110px;height:42px;border:1.5px solid var(--navy-2);color:var(--navy);font-size:14px}

/* Hero */
.hero{top:74px;height:650px;background:var(--warm)}
.hero h1{left:161px;top:38px;font-size:44px;line-height:46px;color:var(--navy)}
.hero .lead{left:161px;top:140px;font-size:13px;line-height:19px;color:var(--muted)}
.hero .cta{left:161px;top:192px;width:150px;height:41px}
.hero .more{left:339px;top:203px}
.assure{left:710px;top:82px;display:grid;grid-template-columns:192px 150px;row-gap:30px}
.assure div{display:flex;align-items:center;gap:16px;font-size:12.5px;line-height:19px;color:var(--ink)}
.assure svg{flex:none}

.cat{top:280px;width:282px;height:191px;border-radius:8px;overflow:hidden}
.cat .tag{position:absolute;left:20px;top:24px;font-size:9px;letter-spacing:.8px;color:var(--gold-deep);font-weight:500}
.cat h3{position:absolute;left:20px;top:42px;font-size:21px;line-height:24px}
.cat p{position:absolute;left:20px;top:98px;width:130px;font-size:8.5px;line-height:13px}
.cat .lm{position:absolute;left:20px;top:153px;font-size:9.5px;display:flex;align-items:center;gap:7px}
.cat .shot{position:absolute;right:16px;top:22px;width:110px;height:150px;border-radius:10px}
.cat-1{left:160px;background:var(--navy);color:#fff}
.cat-1 .shot{background:linear-gradient(160deg,#3A4B66,#1A2A45)}
.cat-2{left:458px;background:var(--sand);color:var(--navy)}
.cat-2 p{color:var(--muted)}
.cat-2 .shot{background:linear-gradient(160deg,#2C3B57,#0F1E38)}
.cat-3{left:756px;background:#DCE5F2;color:var(--navy)}
.cat-3 p{color:var(--muted)}
.cat-3 .shot{background:linear-gradient(160deg,#FFFFFF,#E6ECF4)}

.mini{top:484px;width:168px;height:80px;background:#fff;border-radius:6px;border:1px solid #EEE8E1}
.mini .ic{position:absolute;left:12px;top:20px;width:38px;height:38px;border-radius:50%;background:#F3F0EC;display:flex;align-items:center;justify-content:center}
.mini b{position:absolute;left:64px;top:16px;font-size:8.5px;line-height:11px;font-weight:500;color:var(--navy)}
.mini small{position:absolute;left:64px;top:45px;font-size:7.5px;line-height:10px;color:var(--muted)}
.mini .ar{position:absolute;right:10px;bottom:14px}

.band{top:683px;height:41px;background:var(--sand)}
.band .item{position:absolute;top:10px;display:flex;align-items:center;gap:10px;font-size:12px;color:#C6A57C}

/* Expert */
.expert{top:724px;height:580px;background:var(--warm)}
.expert h2{left:161px;top:86px;font-size:44px;line-height:53px;color:var(--navy)}
.expert .lead{left:161px;top:248px;font-size:13px;line-height:19px;color:var(--muted)}
.checks{left:161px;top:305px;list-style:none;font-size:12px;color:var(--muted)}
.checks li{display:flex;align-items:center;gap:10px;height:29px}
.expert .cta{left:161px;top:412px;width:150px;height:41px}
.expert .more{left:339px;top:423px}
.avatars{left:161px;top:488px;display:flex}
.avatars i{width:36px;height:36px;border-radius:50%;border:2px solid #fff;margin-right:-8px;background:linear-gradient(135deg,#D8B89A,#9C7B62)}
.rating{left:294px;top:485px;font-size:10px;line-height:13px;color:var(--muted)}
.rating .stars{color:var(--gold);font-size:13px;letter-spacing:2px}
.couple{left:560px;top:42px;width:590px;height:538px;border-radius:300px 300px 0 0;background:radial-gradient(ellipse at 50% 40%,#C99F82 0%,#A9826A 35%,#F3EDE7 75%)}
.stat{left:852px;top:322px;width:252px;height:219px;background:#fff;border-radius:14px;box-shadow:0 10px 30px rgba(11,27,51,.08)}
.stat .k{position:absolute;left:20px;top:24px;font-size:11px;letter-spacing:1px;color:var(--navy)}
.stat .v{position:absolute;left:20px;top:42px;font-size:42px;color:var(--navy)}
.stat p{position:absolute;left:20px;top:97px;width:140px;font-size:11px;line-height:14px;color:var(--muted)}
.stat .rule{position:absolute;left:20px;right:20px;top:168px;border-top:1px solid var(--line)}
.stat .foot{position:absolute;left:20px;right:20px;top:186px;display:flex;justify-content:space-between;font-size:11px;color:var(--navy)}

/* Products */
.products{top:1304px;height:607px;background:var(--sky);overflow:hidden}
.sec-title{width:1200px;text-align:center;font-size:44px;color:var(--navy)}
.products .sec-title{top:49px}
.prod{top:136px;width:355px;height:360px;background:var(--paper);border-radius:10px;overflow:hidden}
.prod .tag{position:absolute;left:30px;top:28px;font-size:10.5px;letter-spacing:1px;color:var(--gold-deep);font-weight:500}
.prod h3{position:absolute;left:30px;top:54px;font-size:35px;line-height:39px;color:var(--navy)}
.prod p{position:absolute;left:30px;width:160px;font-size:12px;line-height:18px;color:var(--muted)}
.prod .b1,.prod .b2{position:absolute;left:30px;width:125px;height:33px;font-size:11.5px}
.prod .safety{position:absolute;left:30px;top:323px;font-size:9px;text-decoration:underline;color:var(--navy)}
.prod .shot{position:absolute;border-radius:14px}
.slider{top:528px;display:flex;gap:16px}
.slider span{width:30px;height:30px;border-radius:50%;display:flex;align-items:center;justify-content:center;background:#E4D8C9}

/* How it works */
.how{top:1911px;height:763px;background:#F7F8FB}
.how .sec-title{top:51px}
.step{width:430px;height:228px;background:#fff;border-radius:8px;border:1px solid #EEF0F4}
.step .art{position:absolute;left:12px;top:18px;width:190px;height:192px;border-radius:10px;background:linear-gradient(160deg,#F7EFE6,#ECE4DA)}
.step .num{position:absolute;left:228px;top:34px;width:24px;height:24px;border-radius:50%;background:var(--navy);color:#fff;font-size:11px;font-weight:600;display:flex;align-items:center;justify-content:center}
.step .sic{position:absolute;left:268px;top:28px}
.step h3{position:absolute;left:228px;top:72px;font-size:21px;line-height:27px;color:var(--navy)}
.step p{position:absolute;left:228px;width:180px;font-size:10px;line-height:16px;color:var(--muted)}
.flow{width:26px;height:26px;border-radius:50%;background:#fff;display:flex;align-items:center;justify-content:center}
.how .view{left:526px;top:672px;width:149px;height:42px}

/* Trust */
.trust{top:2674px;height:671px;background:#fff}
.trust .sec-title{top:52px}
.pillar{top:153px;width:254px;height:443px;border:1px solid #EEEAE4;border-radius:16px;text-align:center;background:var(--paper)}
.pillar .ring{margin:40px auto 0;width:136px;height:136px;border-radius:50%;background:#F5F0EA;display:flex;align-items:center;justify-content:center}
.pillar h3{margin-top:26px;font-size:29px;line-height:33px;color:var(--navy)}
.pillar p{margin:48px auto 0;width:200px;font-size:15px;line-height:25px;color:var(--muted)}

/* Newsletter + footer */
.site-foot{top:3345px;height:471px;background:var(--navy);color:#fff}
.site-foot h2{left:160px;top:40px;font-size:57px;line-height:70px}
.signup{left:643px;top:75px;width:395px;height:46px;border-radius:30px;background:#fff;display:flex;align-items:center;justify-content:space-between;padding:0 4px 0 24px;font-size:11.5px;color:#8A909C}
.signup span.go{width:40px;height:40px;border-radius:50%;background:var(--gold);display:flex;align-items:center;justify-content:center}
.rule-f{left:160px;width:878px;border-top:1px solid rgba(255,255,255,.12)}
.foot-logo{left:161px;top:266px;width:174px;height:86px;background:#fff;display:flex;align-items:center;justify-content:center}
.foot-logo .logo{font-size:50px}
.col h4{font-size:15px;font-weight:500;letter-spacing:.5px;margin-bottom:20px}
.col a{display:block;font-size:13.5px;line-height:23px;color:#DDE2EA}
.col .phone{font-size:19px;font-weight:600;margin-top:4px;color:#fff}
.socials{display:flex;gap:30px;align-items:center}
.socials i{width:14px;height:14px;border-radius:50%;background:#fff;display:block}
.legal{top:450px;font-size:10px;color:#D5DAE2}
</style>
</head>
<body>

<header class="site-nav">
  <a class="abs logo" href="#">quellor<span>.</span></a>
  <nav class="abs nav-links">
    <a style="left:0">Treatments <svg width="10" height="8" viewBox="0 0 10 8"><path d="M1 2l4 4 4-4" fill="none" stroke="#1B2333" stroke-width="1.3"/></svg></a>
    <a style="left:144px">How It Works</a>
    <a style="left:301px">About</a>
    <a style="left:414px">FAQs</a>
  </nav>
  <a class="abs btn nav-cta" href="#">Get Started</a>
  <a class="abs btn nav-login" href="#">Log In</a>
</header>

<section class="hero">
  <h1 class="abs serif">Personalized Treatments,<br><span class="gold">Tailored to You.</span></h1>
  <p class="abs lead">Expert care for weight loss and sexual health.<br>100% online. No insurance required.</p>
  <a class="abs btn btn-navy cta" href="#">Get Started <svg width="22" height="10" viewBox="0 0 22 10"><path d="M0 5h20M16 1l4 4-4 4" fill="none" stroke="#E0A458" stroke-width="1.4"/></svg></a>
  <a class="abs link-arrow more" href="#">View All Treatments <svg width="22" height="10" viewBox="0 0 22 10"><path d="M0 5h20M16 1l4 4-4 4" fill="none" stroke="#C98E45" stroke-width="1.4"/></svg></a>
  <div class="abs assure">
    <div><svg width="28" height="30" viewBox="0 0 28 30"><path d="M14 2l11 4v9c0 7-5 11-11 13C8 26 3 22 3 15V6z" fill="none" stroke="#0B1B33" stroke-width="1.5"/><circle cx="14" cy="12" r="3" fill="none" stroke="#0B1B33" stroke-width="1.5"/><path d="M9 20c1-3 3-4 5-4s4 1 5 4" fill="none" stroke="#0B1B33" stroke-width="1.5"/></svg><span>Licensed<br>US providers</span></div>
    <div><svg width="28" height="30" viewBox="0 0 28 30"><path d="M14 3l11 5v13l-11 6-11-6V8z M3 8l11 6 11-6 M14 14v13" fill="none" stroke="#0B1B33" stroke-width="1.5"/></svg><span>Discreet<br>delivery</span></div>
    <div><svg width="28" height="30" viewBox="0 0 28 30"><path d="M14 2l11 4v9c0 7-5 11-11 13C8 26 3 22 3 15V6z" fill="none" stroke="#0B1B33" stroke-width="1.5"/><path d="M9 15l4 4 7-8" fill="none" stroke="#0B1B33" stroke-width="1.5"/></svg><span>FDA-approved<br>medications</span></div>
    <div><svg width="30" height="26" viewBox="0 0 30 26"><rect x="2" y="4" width="26" height="19" rx="3" fill="none" stroke="#0B1B33" stroke-width="1.5"/><path d="M2 10h26" stroke="#0B1B33" stroke-width="1.5"/><rect x="19" y="14" width="6" height="4" rx="1" fill="none" stroke="#0B1B33" stroke-width="1.5"/></svg><span>No insurance<br>required</span></div>
  </div>

  <article class="abs cat cat-1">
    <span class="tag">WEIGHT LOSS</span>
    <h3 class="serif">GLP-1<br>Treatments</h3>
    <p>Clinically proven medications to help you lose weight and keep it off.</p>
    <a class="lm" href="#" style="color:var(--gold)">Learn More <svg width="16" height="16" viewBox="0 0 16 16"><circle cx="8" cy="8" r="7" fill="none" stroke="#fff" stroke-width="1"/><path d="M5 8h6M9 6l2 2-2 2" fill="none" stroke="#fff" stroke-width="1"/></svg></a>
    <div class="shot" role="img" aria-label="Product photo: GLP-1 medication vial"></div>
  </article>
  <article class="abs cat cat-2">
    <span class="tag">SEXUAL HEALTH</span>
    <h3 class="serif">ED Treatments<br>for Men</h3>
    <p>Personalized solutions to improve performance and confidence.</p>
    <a class="lm" href="#" style="color:var(--gold-deep)">Learn More <svg width="16" height="16" viewBox="0 0 16 16"><circle cx="8" cy="8" r="7" fill="none" stroke="#C98E45" stroke-width="1"/><path d="M5 8h6M9 6l2 2-2 2" fill="none" stroke="#C98E45" stroke-width="1"/></svg></a>
    <div class="shot" role="img" aria-label="Product photo: navy medication box with capsules"></div>
  </article>
  <article class="abs cat cat-3">
    <span class="tag" style="color:var(--navy-2)">MEN'S HEALTH</span>
    <h3 class="serif">Hair Loss<br>Treatments</h3>
    <p>Prescription solutions designed to help maintain and regrow hair.</p>
    <a class="lm" href="#" style="color:var(--navy-2)">Learn More <svg width="16" height="16" viewBox="0 0 16 16"><circle cx="8" cy="8" r="7" fill="none" stroke="#14315C" stroke-width="1"/><path d="M5 8h6M9 6l2 2-2 2" fill="none" stroke="#14315C" stroke-width="1"/></svg></a>
    <div class="shot" role="img" aria-label="Product photo: white prescription bottle"></div>
  </article>

  <div class="abs mini" style="left:160px"><span class="ic"><svg width="16" height="18" viewBox="0 0 16 18"><rect x="1.5" y="2" width="13" height="15" rx="2" fill="none" stroke="#0B1B33" stroke-width="1.2"/><path d="M5 7h6M5 10h6M5 13h4" stroke="#0B1B33" stroke-width="1.2"/></svg></span><b>Weight Management<br>Support</b><small>Ongoing provider<br>guidance.</small><svg class="ar" width="12" height="8" viewBox="0 0 12 8"><path d="M0 4h10M7 1l3 3-3 3" fill="none" stroke="#E0A458" stroke-width="1.2"/></svg></div>
  <div class="abs mini" style="left:337px"><span class="ic"><svg width="16" height="18" viewBox="0 0 16 18"><circle cx="8" cy="6" r="3.5" fill="none" stroke="#0B1B33" stroke-width="1.2"/><path d="M2 17c0-4 3-6 6-6s6 2 6 6" fill="none" stroke="#0B1B33" stroke-width="1.2"/></svg></span><b>Personalized<br>Care Plans</b><small>Tailored to<br>your goals.</small><svg class="ar" width="12" height="8" viewBox="0 0 12 8"><path d="M0 4h10M7 1l3 3-3 3" fill="none" stroke="#E0A458" stroke-width="1.2"/></svg></div>
  <div class="abs mini" style="left:514px"><span class="ic"><svg width="20" height="16" viewBox="0 0 20 16"><path d="M1 3h11v9H1zM12 6h4l3 3v3h-7z" fill="none" stroke="#0B1B33" stroke-width="1.2"/><circle cx="5" cy="13" r="1.8" fill="#fff" stroke="#0B1B33" stroke-width="1.2"/><circle cx="15" cy="13" r="1.8" fill="#fff" stroke="#0B1B33" stroke-width="1.2"/></svg></span><b>Discreet Home<br>Delivery</b><small>Medication shipped<br>to your door.</small><svg class="ar" width="12" height="8" viewBox="0 0 12 8"><path d="M0 4h10M7 1l3 3-3 3" fill="none" stroke="#E0A458" stroke-width="1.2"/></svg></div>
  <div class="abs mini" style="left:691px"><span class="ic"><svg width="18" height="16" viewBox="0 0 18 16"><path d="M1.5 1.5h15v10h-9l-4 3v-3h-2z" fill="none" stroke="#0B1B33" stroke-width="1.2"/><path d="M5 5h8M5 8h6" stroke="#0B1B33" stroke-width="1.2"/></svg></span><b>Provider<br>Messaging</b><small>Support whenever<br>you need it.</small><svg class="ar" width="12" height="8" viewBox="0 0 12 8"><path d="M0 4h10M7 1l3 3-3 3" fill="none" stroke="#E0A458" stroke-width="1.2"/></svg></div>
  <div class="abs mini" style="left:868px;width:170px"><span class="ic"><svg width="20" height="16" viewBox="0 0 20 16"><path d="M10 3C7 1 4 1 1 2v12c3-1 6-1 9 1 3-2 6-2 9-1V2c-3-1-6-1-9 1zM10 3v12" fill="none" stroke="#0B1B33" stroke-width="1.2"/></svg></span><b>Wellness<br>Resources</b><small>Education and<br>expert advice.</small><svg class="ar" width="12" height="8" viewBox="0 0 12 8"><path d="M0 4h10M7 1l3 3-3 3" fill="none" stroke="#E0A458" stroke-width="1.2"/></svg></div>
</section>

<div class="abs band" style="left:0;width:1200px;top:683px;height:41px;background:var(--sand)">
  <span class="item" style="left:58px"><svg width="22" height="20" viewBox="0 0 22 20"><rect x="2" y="2" width="14" height="16" rx="1.5" fill="none" stroke="#C6A57C" stroke-width="1.2"/><path d="M5 7h8M5 10h6" stroke="#C6A57C" stroke-width="1.2"/><circle cx="17" cy="14" r="3" fill="none" stroke="#C6A57C" stroke-width="1.2"/></svg>US-Licensed medical providers</span>
  <span class="item" style="left:353px"><svg width="20" height="20" viewBox="0 0 20 20"><rect x="3" y="6" width="14" height="12" rx="2" fill="none" stroke="#C6A57C" stroke-width="1.2"/><path d="M6 6V3h8v3M10 9v6M7 12h6" stroke="#C6A57C" stroke-width="1.2"/></svg>Evidence-based treatments</span>
  <span class="item" style="left:631px"><svg width="22" height="20" viewBox="0 0 22 20"><path d="M11 18S2 12 2 7a4.5 4.5 0 019-1 4.5 4.5 0 019 1c0 5-9 11-9 11z" fill="none" stroke="#C6A57C" stroke-width="1.2"/></svg>Ongoing support at every step</span>
  <span class="item" style="left:907px"><svg width="22" height="20" viewBox="0 0 22 20"><path d="M11 2l8 3v6c0 4-4 7-8 8-4-1-8-4-8-8V5z" fill="none" stroke="#C6A57C" stroke-width="1.2"/><path d="M7 10l3 3 5-6" fill="none" stroke="#C6A57C" stroke-width="1.2"/></svg>Trusted by thousands of patients</span>
</div>

<section class="expert">
  <div class="abs couple" role="img" aria-label="Photo of a smiling couple embracing"></div>
  <h2 class="abs serif">Expert Care,<br>Designed for<br><span class="gold">Real Results.</span></h2>
  <p class="abs lead">Personalized treatments for weight loss and<br>sexual wellness. 100% online. No insurance required.</p>
  <ul class="abs checks">
    <li><svg width="14" height="12" viewBox="0 0 14 12"><path d="M1 6l4 4 8-9" fill="none" stroke="#E0A458" stroke-width="1.6"/></svg>Licensed US providers</li>
    <li><svg width="14" height="12" viewBox="0 0 14 12"><path d="M1 6l4 4 8-9" fill="none" stroke="#E0A458" stroke-width="1.6"/></svg>FDA-approved medications</li>
    <li><svg width="14" height="12" viewBox="0 0 14 12"><path d="M1 6l4 4 8-9" fill="none" stroke="#E0A458" stroke-width="1.6"/></svg>Discreet care and delivery</li>
  </ul>
  <a class="abs btn btn-navy cta" href="#">Get Started <svg width="22" height="10" viewBox="0 0 22 10"><path d="M0 5h20M16 1l4 4-4 4" fill="none" stroke="#E0A458" stroke-width="1.4"/></svg></a>
  <a class="abs link-arrow more" href="#">Check Eligibility <svg width="22" height="10" viewBox="0 0 22 10"><path d="M0 5h20M16 1l4 4-4 4" fill="none" stroke="#C98E45" stroke-width="1.4"/></svg></a>
  <div class="abs avatars" role="img" aria-label="Patient portraits"><i></i><i style="background:linear-gradient(135deg,#C9A48A,#7E5F4C)"></i><i style="background:linear-gradient(135deg,#D9C0A8,#A38267)"></i><i style="background:linear-gradient(135deg,#CDB29C,#8A6A56)"></i></div>
  <div class="abs rating"><div class="stars">★★★★★</div>Trusted by 10,000+<br>patients across the USA</div>
  <div class="abs stat">
    <span class="k">REAL RESULTS</span>
    <span class="v serif">82%</span>
    <p>of patients saw meaningful progress within the first 3 months</p>
    <svg class="abs" style="left:148px;top:50px" width="84" height="100" viewBox="0 0 84 100"><path d="M4 4c30 8 34 26 28 44s2 40 44 46" fill="none" stroke="#E0A458" stroke-width="1.6"/><circle cx="76" cy="94" r="2.5" fill="#E0A458"/></svg>
    <div class="rule"></div>
    <div class="foot"><svg width="10" height="14" viewBox="0 0 10 14"><path d="M5 0v12M1 8l4 4 4-4" fill="none" stroke="#0B1B33" stroke-width="1.2"/></svg><span>Your Journey Starts Here</span></div>
  </div>
</section>

<section class="products">
  <h2 class="abs serif sec-title">Our Products</h2>
  <article class="abs prod" style="left:160px">
    <span class="tag">WEIGHT LOSS</span>
    <h3 class="serif">GLP-1<br>Treatments</h3>
    <p style="top:146px">Clinically proven support for sustainable weight loss.</p>
    <a class="btn btn-navy b1" href="#" style="top:204px">Get Started →</a>
    <a class="btn btn-outline b2" href="#" style="top:248px">Learn More</a>
    <a class="safety" href="#">Important safety information</a>
    <div class="shot" style="left:200px;top:74px;width:140px;height:250px;background:linear-gradient(160deg,#E9EDF3,#B9C2CF 60%,#1B2B45)" role="img" aria-label="Product photo: GLP-1 treatment vial"></div>
  </article>
  <article class="abs prod" style="left:524px">
    <span class="tag">SEXUAL WELLNESS</span>
    <h3 class="serif">Sexual<br>Wellness</h3>
    <p style="top:146px">Personalized treatments designed for confidence and intimate health.</p>
    <a class="btn btn-navy b1" href="#" style="top:218px">Get Started →</a>
    <a class="btn btn-outline b2" href="#" style="top:262px">Learn More</a>
    <a class="safety" href="#">Important safety information</a>
    <div class="shot" style="left:230px;top:24px;width:60px;height:300px;background:linear-gradient(180deg,#F1F2F5,#D5D9E0 55%,#1B2B45)" role="img" aria-label="Product photo: spray pen applicator"></div>
  </article>
  <article class="abs prod" style="left:889px">
    <span class="tag">HAIR HEALTH</span>
    <h3 class="serif">Hair Loss<br>Treatments</h3>
    <p style="top:146px">Prescription solutions to help maintain and regrow hair.</p>
    <a class="btn btn-navy b1" href="#" style="top:218px">Get Started →</a>
    <a class="btn btn-outline b2" href="#" style="top:262px">Learn More</a>
    <a class="safety" href="#">Important safety information</a>
    <div class="shot" style="left:210px;top:80px;width:150px;height:220px;background:linear-gradient(180deg,#F4F5F8 0%,#E4E7EC 25%,#14223B 30%)" role="img" aria-label="Product photo: hair loss treatment bottle"></div>
  </article>
  <div class="abs slider" style="left:960px">
    <span><svg width="8" height="12" viewBox="0 0 8 12"><path d="M6 1L1 6l5 5" fill="none" stroke="#0B1B33" stroke-width="1.4"/></svg></span>
    <span><svg width="8" height="12" viewBox="0 0 8 12"><path d="M2 1l5 5-5 5" fill="none" stroke="#0B1B33" stroke-width="1.4"/></svg></span>
  </div>
</section>

<section class="how">
  <h2 class="abs serif sec-title">How It Works</h2>
  <article class="abs step" style="left:160px;top:151px">
    <div class="art" role="img" aria-label="Illustration: woman filling out an assessment on her phone"></div>
    <span class="num">1</span>
    <svg class="sic" width="20" height="26" viewBox="0 0 20 26"><rect x="1.5" y="3" width="17" height="21" rx="2" fill="none" stroke="#E0A458" stroke-width="1.3"/><path d="M6 3V1h8v2M6 12h8M6 16h8M6 20h5" stroke="#E0A458" stroke-width="1.3"/></svg>
    <h3 class="serif">Complete Your<br>Online Assessment</h3>
    <p style="top:148px">Answer a few simple questions about your health, goals, and medical history.</p>
  </article>
  <article class="abs step" style="left:608px;top:151px">
    <div class="art" role="img" aria-label="Illustration: doctor on a video call screen"></div>
    <span class="num">2</span>
    <svg class="sic" width="24" height="26" viewBox="0 0 24 26"><circle cx="12" cy="7" r="5" fill="none" stroke="#E0A458" stroke-width="1.3"/><path d="M2 25c0-6 4-9 10-9s10 3 10 9" fill="none" stroke="#E0A458" stroke-width="1.3"/></svg>
    <h3 class="serif">Complete With a<br>Licensed Provider</h3>
    <p style="top:148px">A US-licensed provider reviews your answers and creates a personalized treatment plan.</p>
  </article>
  <article class="abs step" style="left:160px;top:389px">
    <div class="art" role="img" aria-label="Illustration: navy treatment box with bottle and capsules"></div>
    <span class="num">3</span>
    <svg class="sic" width="30" height="22" viewBox="0 0 30 22"><path d="M1 3h17v13H1zM18 7h6l5 5v4H18z" fill="none" stroke="#E0A458" stroke-width="1.3"/><circle cx="7" cy="18" r="2.5" fill="#fff" stroke="#E0A458" stroke-width="1.3"/><circle cx="23" cy="18" r="2.5" fill="#fff" stroke="#E0A458" stroke-width="1.3"/></svg>
    <h3 class="serif">Receive Your<br>Treatment</h3>
    <p style="top:148px">If prescribed, your medication is discreetly packaged and shipped to your door.</p>
  </article>
  <article class="abs step" style="left:608px;top:389px">
    <div class="art" role="img" aria-label="Illustration: woman messaging her care team"></div>
    <span class="num">4</span>
    <svg class="sic" width="26" height="24" viewBox="0 0 26 24"><path d="M13 22S2 15 2 8a5.5 5.5 0 0111-1.5A5.5 5.5 0 0124 8c0 7-11 14-11 14z" fill="none" stroke="#E0A458" stroke-width="1.3"/></svg>
    <h3 class="serif">Ongoing Support<br>Every Step of<br>The Way</h3>
    <p style="top:158px">Message your care team anytime and get the support you need to reach your goals.</p>
  </article>
  <span class="abs flow" style="left:588px;top:250px"><svg width="14" height="10" viewBox="0 0 14 10"><path d="M0 5h12M8 1l4 4-4 4" fill="none" stroke="#E0A458" stroke-width="1.4"/></svg></span>
  <span class="abs flow" style="left:588px;top:488px"><svg width="14" height="10" viewBox="0 0 14 10"><path d="M0 5h12M8 1l4 4-4 4" fill="none" stroke="#E0A458" stroke-width="1.4"/></svg></span>
  <a class="abs btn btn-navy view" href="#">View All <svg width="22" height="10" viewBox="0 0 22 10"><path d="M0 5h20M16 1l4 4-4 4" fill="none" stroke="#E0A458" stroke-width="1.4"/></svg></a>
</section>

<section class="trust">
  <h2 class="abs serif sec-title">Care You Can Trust</h2>
  <article class="abs pillar" style="left:54px">
    <div class="ring"><svg width="92" height="104" viewBox="0 0 92 104"><path d="M46 4l40 14v30c0 26-18 42-40 52C24 90 6 74 6 48V18z" fill="#fff" stroke="#0B1B33" stroke-width="3"/><circle cx="46" cy="44" r="10" fill="none" stroke="#E0A458" stroke-width="3"/><path d="M28 74c3-10 10-14 18-14s15 4 18 14z" fill="none" stroke="#E0A458" stroke-width="3"/></svg></div>
    <h3 class="serif">Licensed<br>US Providers</h3>
    <p>Board-certified healthcare professionals focused on your goals.</p>
  </article>
  <article class="abs pillar" style="left:332px">
    <div class="ring"><svg width="80" height="80" viewBox="0 0 80 80"><path d="M40 4l10 8 12-2 4 12 10 6-4 12 4 12-10 6-4 12-12-2-10 8-10-8-12 2-4-12-10-6 4-12-4-12 10-6 4-12 12 2z" fill="#fff" stroke="#0B1B33" stroke-width="3"/><circle cx="40" cy="40" r="16" fill="none" stroke="#E0A458" stroke-width="3"/><path d="M32 40l6 6 11-12" fill="none" stroke="#E0A458" stroke-width="3"/></svg></div>
    <h3 class="serif">FDA-Approved<br>Medications</h3>
    <p>Evidence-based treatments prescribed when clinically appropriate.</p>
  </article>
  <article class="abs pillar" style="left:610px">
    <div class="ring"><svg width="70" height="96" viewBox="0 0 70 96"><path d="M17 40V26a18 18 0 0136 0v14" fill="none" stroke="#0B1B33" stroke-width="3"/><rect x="5" y="40" width="60" height="50" rx="6" fill="#fff" stroke="#0B1B33" stroke-width="3"/><circle cx="35" cy="60" r="6" fill="#E0A458"/><path d="M35 64v12" stroke="#E0A458" stroke-width="4"/></svg></div>
    <h3 class="serif">Private &amp;<br>Secure</h3>
    <p>Your health information is protected with industry-leading privacy standards.</p>
  </article>
  <article class="abs pillar" style="left:889px">
    <div class="ring"><svg width="104" height="66" viewBox="0 0 104 66"><path d="M24 6h46v40H24zM70 18h16l14 14v14H70z" fill="#fff" stroke="#0B1B33" stroke-width="3"/><circle cx="38" cy="50" r="7" fill="#fff" stroke="#0B1B33" stroke-width="3"/><circle cx="84" cy="50" r="7" fill="#fff" stroke="#0B1B33" stroke-width="3"/><path d="M2 18h16M6 28h14M2 38h16" stroke="#E0A458" stroke-width="3"/></svg></div>
    <h3 class="serif">Discreet<br>Delivery</h3>
    <p>Medications shipped directly to your door in plain packaging.</p>
  </article>
</section>

<footer class="site-foot">
  <h2 class="abs serif">Subscribe to our<br>newsletter!</h2>
  <div class="abs signup"><span>Your email address</span><span class="go"><svg width="16" height="10" viewBox="0 0 16 10"><path d="M0 5h14M10 1l4 4-4 4" fill="none" stroke="#fff" stroke-width="1.4"/></svg></span></div>
  <div class="abs rule-f" style="top:212px"></div>
  <div class="abs foot-logo"><span class="logo">quellor<span>.</span></span></div>
  <div class="abs col" style="left:403px;top:256px">
    <h4>Useful Link</h4>
    <div style="display:flex;gap:40px"><div><a href="#">How It Works</a><a href="#">About Us</a><a href="#">Patient Reviews</a><a href="#">Blog</a></div><div><a href="#">Careers</a><a href="#">Contact</a></div></div>
  </div>
  <div class="abs col" style="left:678px;top:256px">
    <h4>Contact Us</h4>
    <a href="#">info@quellor.example</a>
    <a class="phone" href="#">1-555-014-2290</a>
  </div>
  <div class="abs col" style="left:938px;top:256px">
    <h4>Our Social</h4>
    <div class="socials" aria-label="Social links"><i></i><i></i><i></i></div>
  </div>
  <div class="abs rule-f" style="top:421px"></div>
  <p class="abs legal" style="left:161px">Copyright © 2026 quellor, All Rights Reserved.</p>
  <p class="abs legal" style="left:843px;display:flex;gap:20px"><a href="#">Teams &amp; Conditions</a><a href="#">Privacy Policy</a></p>
</footer>

</body>
</html>
```